Website for premium health insurance and concierge medicine

This is a brand new website for Brask Insurance Services that specializes in Health Insurance and Concierge Medicine for high net-worth and affluent individuals and families. Through this website, clients will be able to learn about products and services, submit applications, and complete self enrollment forms. The website needs to have a premium look & feel that will appeal to a discerning high net-worth individual.

I’m looking for 4 pages in total to begin with. I’m also looking for a designer who will be interested in continuing to build out this new site further over the next few months.

The headline for each page is listed below:

Page 1: HOME PAGE
“Premium Healthcare | Bespoke Concierge Services | Absolute Peace of Mind.”

Page 2: HEALTH INSURANCE
“Premium Healthcare | Elevated.”

Page 3: CONCIERGE MEDICINE
“Personalized Medicine | At-Home Concierge Care | Your Private Physician, 24/7.”

Page 4: DENTAL & VISION
“Your Smile | Your Vision | Perfected.”

Here are several links to existing websites that can be used as design inspiration:

https://vantromhealth.com
https://www.pelvix.org/specialties-services/other-programs-services/concierge-medicine
https://wardelmdnx.com

More generally speaking, I like a clean, modern, dutch style of websites. Here’s an unrelated site that has a good design:

https://www.morvathis.com

Here are a few additional phrases and keywords that will help inspire the design:

Premium Health Insurance
Executive Health Insurance
Concierge Medicine
24/7 access dedicated concierge team
Integrative Concierge Care

I will upload logo files below, here are the font & colors information:

Font: Trajan Pro Bold
Colors:
Blue: hex code: 0071BD, Rgb code: 0, 113, 189  cmyk code: 87,53,0,0
Gray: hex code: #666666, Rgb code: 102,102,102 cmyk code: 60,51,51,20

```html
<!DOCTYPE html>
<html lang="en">
<head>
<meta charset="utf-8">
<title>Brask Insurance Services | Premium Healthcare Elevated</title>
<link href="https://fonts.googleapis.com/css2?family=Libre+Baskerville&family=Inter:wght@400;500;600&display=swap" rel="stylesheet">
<style>
:root{
  --brand-blue:#0071BD;
  --brand-gray:#666666;
  --ink:#222222;
  --muted:#444444;
  --line:#cfd6dc;
  --footer-bg:#232323;
  --footer-text:#e6e6e6;
  --white:#ffffff;
}
*{margin:0;padding:0;box-sizing:border-box}
html,body{width:1200px;height:2506px;overflow:hidden;background:var(--white)}
body{position:relative;font-family:"Inter",sans-serif;color:var(--ink)}
.abs{position:absolute}
.serif{font-family:"Libre Baskerville",serif;font-weight:400}

/* header */
.brand{left:58px;top:24px;display:flex;align-items:center;gap:8px;color:var(--brand-blue);font-family:"Libre Baskerville",serif;font-size:13px;line-height:1.1;width:110px}
.brand-mark{width:10px;height:10px;background:var(--brand-blue);flex:none}
.nav{top:31px;left:601px;display:flex;gap:35px;font-size:8.5px;color:var(--ink);line-height:14px}
.btn-login{left:915px;top:27px;width:73px;height:23px;border-radius:12px;background:var(--brand-blue);color:var(--white);font-size:8.5px;display:flex;align-items:center;justify-content:center;gap:6px}
.search{left:1010px;top:27px;width:128px;height:23px;border:1px solid var(--line);border-radius:12px;font-size:8px;color:#aab;padding-left:13px;display:flex;align-items:center}
.search svg{position:absolute;right:12px;top:7px}

.page-title{left:54px;top:96px;font-size:31px;color:#333}
.hero{left:0;top:159px;width:1200px;height:361px;background:linear-gradient(180deg,#c9d4dc 0%,#e6d9cf 45%,#b8c3cb 80%,#d5dbe0 100%)}

.intro-title{left:0;width:1200px;top:555px;text-align:center;font-size:20px;color:#333}
.intro-text{left:150px;width:900px;top:645px;text-align:center;font-size:9.5px;line-height:15px;color:var(--muted)}

/* features */
.feature{width:420px}
.feature h3{font-family:"Libre Baskerville",serif;font-weight:400;font-size:20px;color:#333;display:inline-block}
.feature p{font-size:9.5px;line-height:15px;color:var(--muted);margin-top:24px}
.arrow-box{position:absolute;top:-10px;width:34px;height:34px;border:1px solid #555;border-radius:4px;display:flex;align-items:center;justify-content:center}

/* split */
.split-img{background:linear-gradient(135deg,#2e5966 0%,#8fc7d0 45%,#d6eef0 60%,#3c6b78 100%)}
.split-img.team{background:linear-gradient(120deg,#1f3e47 0%,#6fa9b5 40%,#cfe6ea 62%,#2d4f59 100%)}
.split-text h4{font-size:14px;font-weight:600;color:#333}
.split-text p{font-size:9.5px;line-height:15px;color:var(--muted);margin-top:32px;width:350px}

/* cta */
.cta{left:0;top:1588px;width:1200px;height:675px;background:radial-gradient(ellipse at 50% 55%,#2c3b3f 0%,#1b2528 55%,#111719 100%)}
.cta-title{left:0;width:1200px;top:1833px;text-align:center;color:var(--white);font-size:20px}
.cta-text{left:425px;width:350px;top:1889px;text-align:center;color:#e9eef0;font-size:11px;line-height:15px}
.cta-btn{left:485px;top:1989px;width:230px;height:36px;border:1px solid #6f8fb0;border-radius:4px;background:rgba(120,140,170,.35);color:var(--white);font-size:13px;display:flex;align-items:center;justify-content:center}

/* footer */
.footer{left:0;top:2263px;width:1200px;height:243px;background:var(--footer-bg)}
.footer-brand{left:72px;top:2358px;display:flex;align-items:center;gap:12px;color:var(--white);font-family:"Libre Baskerville",serif;font-size:19px;line-height:1.2;width:200px}
.footer-brand .brand-mark{width:16px;height:16px}
.fcol{top:2323px;font-size:7.5px;color:var(--footer-text)}
.fcol h5{font-weight:500;font-size:7.5px;margin-bottom:18px}
.fcol li{list-style:none;margin-bottom:8px}
.copyright{left:415px;top:2420px;font-size:7.5px;color:var(--footer-text)}
</style>
</head>
<body>

<header>
  <div class="abs brand"><span class="brand-mark"></span><span>Brask Insurance Services</span></div>
  <nav class="abs nav"><span>Health Insurance</span><span>Concierge Medicine</span><span>Dental &amp; Vision</span></nav>
  <div class="abs btn-login">Login
    <svg width="9" height="7" viewBox="0 0 9 7"><path d="M0 3.5H8M5 0.5L8 3.5L5 6.5" stroke="#fff" fill="none"/></svg>
  </div>
  <div class="abs search">Search
    <svg width="8" height="8" viewBox="0 0 8 8"><circle cx="3.3" cy="3.3" r="2.6" stroke="#aab" fill="none"/><path d="M5.2 5.2L7.5 7.5" stroke="#aab"/></svg>
  </div>
</header>

<h1 class="abs serif page-title">Premium Healthcare | Elevated</h1>
<div class="abs hero" role="img" aria-label="Medical professional seated at a futuristic workstation overlooking a city skyline at sunrise"></div>

<h2 class="abs serif intro-title">Tailored Coverage for Those Who Demand the Best</h2>
<p class="abs intro-text">Your health is your most valuable asset—protect it with exclusive, high-end insurance plans designed for discerning individuals and families. Our premium health insurance solutions provide access to world-class private healthcare, top specialists, and global medical coverage, ensuring that you receive the very best care, no matter where you are</p>

<section>
  <div class="abs feature" style="left:123px;top:764px">
    <h3>Global Coverage</h3>
    <span class="arrow-box" style="left:202px"><svg width="12" height="12" viewBox="0 0 12 12"><path d="M1 1L11 11M4 11H11V4" stroke="#333" fill="none" stroke-width="1.2"/></svg></span>
    <p>Access top tier private hospitals and specialist worldwide</p>
  </div>
  <div class="abs feature" style="left:699px;top:764px">
    <h3>Personal Health Plans</h3>
    <span class="arrow-box" style="left:253px"><svg width="12" height="12" viewBox="0 0 12 12"><path d="M1 1L11 11M4 11H11V4" stroke="#333" fill="none" stroke-width="1.2"/></svg></span>
    <p>Designed to fit your lifestyle, needs and priorities</p>
  </div>
  <div class="abs feature" style="left:123px;top:877px">
    <h3>VIP Medical Concierge</h3>
    <span class="arrow-box" style="left:263px"><svg width="12" height="12" viewBox="0 0 12 12"><path d="M1 1L11 11M4 11H11V4" stroke="#333" fill="none" stroke-width="1.2"/></svg></span>
    <p>Dedicated support for appointments, claims and fast-track approval</p>
  </div>
  <div class="abs feature" style="left:699px;top:877px">
    <h3>Exclusive Network</h3>
    <span class="arrow-box" style="left:223px"><svg width="12" height="12" viewBox="0 0 12 12"><path d="M1 1L11 11M4 11H11V4" stroke="#333" fill="none" stroke-width="1.2"/></svg></span>
    <p>Direct access to elite healthcare providers, executive wellness programs and advanced treatments</p>
  </div>
</section>

<section>
  <div class="abs split-text" style="left:155px;top:1065px">
    <h4>Healthcare Without Limits</h4>
    <p>Whether you require routine check-ups, advanced medical procedures, or specialized treatment abroad, our plans provide seamless coverage and priority access to the best healthcare facilities across the globe. With Brask Insurance, you get more than just coverage—you get peace of mind and unparalleled service.</p>
  </div>
  <div class="abs split-img" style="left:598px;top:1010px;width:535px;height:257px" role="img" aria-label="Futuristic private treatment suite with teal lighting and monitors"></div>
  <div class="abs split-img team" style="left:62px;top:1267px;width:536px;height:256px" role="img" aria-label="Two medical professionals reviewing patient documents together"></div>
  <div class="abs split-text" style="left:691px;top:1321px">
    <h4>Designed for Your Lifestyle</h4>
    <p>We cater to high-net-worth individuals, entrepreneurs, executives, and frequent travelers who need flexible, global healthcare solutions that match their lifestyle. Our dedicated advisors work closely with you to create a customized plan that ensures you receive the highest quality care—whenever, wherever.</p>
  </div>
</section>

<section>
  <div class="abs cta" role="img" aria-label="Dimly lit high-tech medical imaging room"></div>
  <h2 class="abs serif cta-title">Start Your Journey to Exceptional Healthcare</h2>
  <p class="abs cta-text">Secure your health with a plan designed for excellence. Request a private consultation today to explore our exclusive health insurance options.</p>
  <div class="abs cta-btn">Get Started</div>
</section>

<footer>
  <div class="abs footer"></div>
  <div class="abs footer-brand"><span class="brand-mark"></span><span>Brask Insurance Services</span></div>
  <div class="abs fcol" style="left:415px"><h5>Capabilities</h5><ul><li>Technology</li><li>Design</li><li>Expertise</li></ul></div>
  <div class="abs fcol" style="left:580px"><h5>Company</h5><ul><li>About Us</li><li>Contact Us</li><li>Carriers</li></ul></div>
  <div class="abs fcol" style="left:746px"><h5>Legal</h5><ul><li>Privacy Policy</li><li>Terms and Conditions</li><li>Corporate policies</li></ul></div>
  <div class="abs fcol" style="left:947px"><h5>Contacts</h5><ul><li>+415 55502918</li><li>+415 55502918</li><li>+415 55502918</li></ul></div>
  <p class="abs copyright">© Copyright 2025 Brask Insurance All Rights Reserved.</p>
</footer>

</body>
</html>
```